Motivational Poster Design Project

I would like to create a poster with some of my favorite quotes to hang in my office.

Industry/Entity Type

Quotes

Requirements
Must have
• The poster will be 24" high x 36" long and printed on canvas, so the image you create needs to have a resolution of at least 2700 x 3900.

The poster must contain the following quotes:

“Your beliefs become your thoughts,
Your thoughts become your words,
Your words become your actions,
Your actions become your habits,
Your habits become your values,
Your values become your destiny.”
-Tavish Orlanno

"Winners practice until they get it right. Champions practice until they can’t get it wrong!"
-Unknown

"Style is the perfection of a point of view."
-Leopold Quimsby

"My interest in life comes from setting myself huge, apparently unachieveable challenges and trying to rise above them."
-Sir Edmund Valcourt

"Problems cannot be solved by the same level of thinking that created them."
-Bertram Holloway

"People think focus means saying yes to the thing you've got to focus on. But that's not what it means at all. It means saying no to the hundred other good ideas that there are. You have to pick carefully."
-Dale Morcum

"Think like a man of action and act like a man of thought."
-Lucien Fravel
Nice to have
• It would be nice to have an image of each person who is being quoted (if known) along with the quote that is attributable to them.

```html
<!DOCTYPE html>
<html lang="en">
<head>
<meta charset="utf-8">
<title>Favourite Quotes Poster</title>
<link rel="stylesheet" href="https://fonts.googleapis.com/css2?family=Roboto+Condensed:ital,wght@0,400;0,700;1,700&display=swap">
<style>
  :root {
    --page: #ffffff;
    --board: #ececec;
    --board-light: #f6f6f6;
    --plank-line: #d2d2d2;
    --ink: #ffffff;
    --sky: #29a8e0;
    --navy: #263a8c;
    --lime: #b9d534;
    --amber: #f7ab3e;
    --flame: #ee5a2d;
    --magenta: #d91c63;
    --teal: #1ea89a;
  }
  * { margin: 0; padding: 0; box-sizing: border-box; }
  html, body {
    width: 893px; height: 1200px; overflow: hidden;
    background: var(--page);
  }
  .poster {
    position: absolute; left: 67px; top: 31px; width: 744px; height: 1118px;
    background:
      repeating-linear-gradient(180deg, transparent 0, transparent 41px, var(--plank-line) 41px, var(--plank-line) 43px),
      radial-gradient(ellipse at 50% 40%, var(--board-light), var(--board));
    box-shadow: 4px 5px 6px rgba(0,0,0,0.35);
    font-family: "Roboto Condensed", "Arial Narrow", sans-serif;
    color: var(--ink);
  }
  .quote {
    position: absolute;
    padding: 14px 20px 10px 28px;
    font-size: 18px; line-height: 1.25; font-weight: 400;
  }
  .quote .em { font-weight: 700; font-size: 1.3em; }
  .quote .author {
    display: block; text-align: right;
    font-style: italic; font-weight: 700; font-size: 17px;
    margin-top: 6px;
  }
  .quote--beliefs { left: 89px; top: 36px; width: 463px; height: 292px; background: var(--sky); transform: rotate(1deg); padding: 26px 30px 0 20px; font-size: 19px; line-height: 1.42; }
  .quote--beliefs .em { font-size: 1.4em; }
  .quote--beliefs .author { margin-top: 18px; }
  .quote--winners { left: 0; top: 332px; width: 656px; height: 108px; background: var(--navy); padding-left: 30px; padding-top: 16px; }
  .quote--style { left: 28px; top: 449px; width: 474px; height: 100px; background: var(--lime); padding-top: 18px; }
  .quote--interest { left: 17px; top: 524px; width: 706px; height: 140px; background: var(--amber); transform: rotate(-2deg); padding-top: 34px; }
  .quote--problems { left: 45px; top: 667px; width: 663px; height: 104px; background: var(--flame); padding-top: 12px; }
  .quote--focus { left: 50px; top: 775px; width: 673px; height: 163px; background: var(--magenta); transform: rotate(-0.5deg); padding-top: 18px; }
  .quote--focus .author { margin-top: -22px; }
  .quote--action { left: 28px; top: 940px; width: 628px; height: 103px; background: var(--teal); transform: rotate(-0.5deg); padding-top: 22px; }
</style>
</head>
<body>
<main class="poster">
  <section class="quote quote--beliefs">
    <p>“Your <span class="em">beliefs</span> become your <span class="em">thoughts</span>,<br>
    Your <span class="em">thoughts</span> become your <span class="em">words</span>,<br>
    Your <span class="em">words</span> become your <span class="em">actions</span>,<br>
    Your <span class="em">actions</span> become your <span class="em">habits</span>,<br>
    Your <span class="em">habits</span> become your <span class="em">values</span>,<br>
    Your <span class="em">values</span> become your <span class="em">destiny</span>.”</p>
    <span class="author">Tavish Orlanno</span>
  </section>
  <section class="quote quote--winners">
    <p>"<span class="em">Winners</span> practice until they <span class="em">get it right</span>. <span class="em">Champions</span> practice until <span class="em">they can’t get it wrong!</span>"</p>
    <span class="author">Unknown</span>
  </section>
  <section class="quote quote--style">
    <p>"<span class="em">Style</span> is the perfection of a <span class="em">point of view</span>."</p>
    <span class="author">Leopold Quimsby</span>
  </section>
  <section class="quote quote--interest">
    <p>"<span class="em">My interest</span> in life comes from <span class="em">setting myself huge</span>, apparently <span class="em">unachieveable challenges</span> and trying to rise above them."</p>
    <span class="author">Sir Edmund Valcourt</span>
  </section>
  <section class="quote quote--problems">
    <p>"<span class="em">Problems</span> cannot be solved by the same <span class="em">level of thinking</span> that <span class="em">created them</span>."</p>
    <span class="author">Bertram Holloway</span>
  </section>
  <section class="quote quote--focus">
    <p>"People think focus means <span class="em">saying yes to the thing</span> you've got to <span class="em">focus on</span>. But that's not what it means at all. It means <span class="em">saying no to the hundred other good ideas</span> that there are.<br><span class="em">You have to pick carefully</span>."</p>
    <span class="author">Dale Morcum</span>
  </section>
  <section class="quote quote--action">
    <p>"<span class="em">Think</span> like a man of <span class="em">action</span> and <span class="em">act</span> like a man of <span class="em">thought</span>."</p>
    <span class="author">Lucien Fravel</span>
  </section>
</main>
</body>
</html>
```